Nursing Concepts Diagram

We are looking to make a diagram to represent the Conceptual Framework of our nursing program (college). The frame work is based on three parts:

I. Nursing Process

II. Core Concepts
a. Clinical Competence
b. Critical Thinking
c. Moral/Ethical Principles
d. Growth Mindset
e. Caring/Compassion
f. Cultural Competence
g. Effective Communication
h. Life-long Learning

III. Brennick's Hierarchy of Needs

I have attached two sketches to give you a sense of how I think this could work.

Please also consider the following:

-Brennick's Hierarchy of Needs is always represented in the shape of a pyramid so I think the other two components (Nursing Process and Core Concepts) should complement that.

Target Market(s)

Healthcare Professionals, Nursing Educators

Font styles to use
Sans Serif

Colors

Designer to choose colors to be used in the design.

Requirements
Must have
• We would like the diagram to include a legend somewhere on the paper that outlines the parts of each component like demonstrated in the attached table
• All the small parts of the Nursing Process and Brennick's Hierarchy of Needs don't need to be listed out in the diagram because it may look too wordy, but the eight parts that make up the core concepts should all be listed
• The Nursing Process and Brennick's Hierachy of needs should both border each of the 8 core concepts so that it can show a relation.

```html
<!DOCTYPE html>
<html lang="en">
<head>
<meta charset="utf-8">
<title>Nursing Concepts Framework</title>
<link rel="stylesheet" href="https://fonts.googleapis.com/css2?family=Arimo:wght@400;700&family=Tinos&family=Comfortaa:wght@400&display=swap">
<style>
  :root {
    --white: #ffffff;
    --ink: #111111;
    --sky: #27aae1;
    --ocean: #1278bf;
    --navy: #283891;
    --band-light: #2ba0dc;
    --band-dark: #1668b4;
    --grey-light: #f2f2f2;
    --grey-mid: #d4d4d4;
    --grey-dark: #b4b4b4;
    --rule: #ffffff;
    --footer: #070707;
  }
  html, body { margin: 0; padding: 0; overflow: hidden; background: var(--white); }
  .canvas { width: 927px; height: 1200px; overflow: hidden; position: relative; background: var(--white); }
  .stage { width: 1000px; height: 1294px; position: absolute; top: 0; left: 0; transform: scale(0.927); transform-origin: 0 0; }
  .framework { position: absolute; top: 0; left: 0; width: 1000px; height: 700px; }
  .framework .title { font-family: "Tinos", "Times New Roman", serif; font-size: 58px; fill: var(--ink); }
  .framework .concept { font-family: "Arimo", Arial, sans-serif; font-size: 21px; fill: var(--ink); text-anchor: middle; }
  .framework .pyramid-label { font-family: "Comfortaa", "Arimo", sans-serif; font-size: 29px; fill: var(--ink); text-anchor: middle; }
  .nurse-figure { position: absolute; border-radius: 40% 40% 18% 18%; background: linear-gradient(180deg, #8a5a36 0%, #f3d2c4 45%, #ffffff 75%, #e6e6e6 100%); }
  .nurse-figure.main { left: 470px; top: 262px; width: 80px; height: 124px; }
  .nurse-figure.key { left: 163px; top: 744px; width: 66px; height: 102px; }
  .key-icon { position: absolute; }
  .legend { position: absolute; top: 881px; left: 59px; display: flex; gap: 3px; height: 359px; }
  .legend-column { width: 294px; box-sizing: border-box; padding: 30px 0 0 25px; color: var(--white); font-family: "Arimo", Arial, sans-serif; }
  .legend-column.process { background: var(--sky); }
  .legend-column.concepts { background: var(--ocean); }
  .legend-column.needs { background: var(--navy); padding-left: 27px; }
  .legend-column h2 { margin: 0 0 32px; font-size: 24px; font-weight: 700; line-height: 29px; }
  .legend-column.needs h2 { margin-bottom: 16px; }
  .legend-column ul { list-style: none; margin: 0; padding: 0; }
  .legend-column li { font-size: 19px; line-height: 29.5px; position: relative; padding-left: 22px; }
  .legend-column.needs li { padding-left: 34px; }
  .legend-column li::before { content: ""; position: absolute; left: 0; top: 9px; width: 12px; height: 12px; border-radius: 50%; background: var(--white); }
  .legend-column.needs li::before { left: 2px; }
  .footer-band { position: absolute; left: 0; top: 1240px; width: 1000px; height: 54px; background: var(--footer); }
</style>
</head>
<body>
<div class="canvas">
  <div class="stage">
    <svg class="framework" viewBox="0 0 1000 700" aria-label="Nursing framework diagram">
      <defs>
        <linearGradient id="capBody" x1="0" y1="0" x2="0" y2="1">
          <stop offset="0" stop-color="var(--grey-mid)"/>
          <stop offset="0.5" stop-color="var(--grey-light)"/>
          <stop offset="1" stop-color="var(--grey-dark)"/>
        </linearGradient>
        <linearGradient id="capDome" x1="0" y1="0" x2="0" y2="1">
          <stop offset="0" stop-color="#e9e9e9"/>
          <stop offset="1" stop-color="#c9c9c9"/>
        </linearGradient>
        <linearGradient id="capBand" x1="0" y1="0" x2="1" y2="0">
          <stop offset="0" stop-color="var(--band-dark)"/>
          <stop offset="0.5" stop-color="var(--band-light)"/>
          <stop offset="1" stop-color="var(--band-dark)"/>
        </linearGradient>
        <linearGradient id="pyramid" x1="0" y1="0" x2="0" y2="1">
          <stop offset="0" stop-color="#2fb2ea"/>
          <stop offset="1" stop-color="#1d86cf"/>
        </linearGradient>
        <radialGradient id="shadow">
          <stop offset="0" stop-color="#000" stop-opacity="0.35"/>
          <stop offset="1" stop-color="#000" stop-opacity="0"/>
        </radialGradient>
      </defs>
      <ellipse cx="510" cy="605" rx="340" ry="50" fill="url(#shadow)"/>
      <path class="cap-dome" d="M248,280 Q262,196 330,186 Q510,170 700,190 Q760,200 772,280 Q510,248 248,280 Z" fill="url(#capDome)"/>
      <text class="title" x="510" y="245" text-anchor="middle">Nursing Process</text>
      <path class="cap-body" d="M122,352 Q510,268 897,352 L765,585 L258,585 Z" fill="url(#capBody)"/>
      <path class="cap-band" d="M103,315 Q510,220 917,315 L897,352 Q510,268 122,352 Z" fill="url(#capBand)"/>

      <g class="concepts-left">
        <text class="concept" x="313" y="367">Clinical Competence</text>
        <line x1="215" y1="385" x2="405" y2="385" stroke="var(--rule)" stroke-width="2"/>
        <text class="concept" x="307" y="417">Critical Thinking</text>
        <line x1="232" y1="437" x2="388" y2="437" stroke="var(--rule)" stroke-width="2"/>
        <text class="concept" x="310" y="478">Growth Mindset</text>
        <line x1="232" y1="500" x2="388" y2="500" stroke="var(--rule)" stroke-width="2"/>
        <text class="concept" x="306" y="528">Moral/Ethical</text>
        <text class="concept" x="309" y="550">Principles</text>
      </g>
      <g class="concepts-right">
        <text class="concept" x="724" y="368">Cultural Competence</text>
        <line x1="638" y1="385" x2="812" y2="385" stroke="var(--rule)" stroke-width="2"/>
        <text class="concept" x="721" y="417">Caring/Compassion</text>
        <line x1="638" y1="437" x2="795" y2="437" stroke="var(--rule)" stroke-width="2"/>
        <text class="concept" x="719" y="469">Effective</text>
        <text class="concept" x="721" y="490">Communication</text>
        <line x1="638" y1="500" x2="795" y2="500" stroke="var(--rule)" stroke-width="2"/>
        <text class="concept" x="717" y="530">Life-long</text>
        <text class="concept" x="719" y="551">Learning</text>
      </g>

      <path class="pyramid-shape" d="M512,378 L650,555 L372,555 Z" fill="url(#pyramid)"/>
      <text class="pyramid-label" x="512" y="470">Brennick's</text>
      <text class="pyramid-label" x="512" y="506">Hierarchy</text>
      <text class="pyramid-label" x="512" y="542">of Needs</text>
    </svg>
    <div class="nurse-figure main" role="img" aria-label="Illustrated nurse in cap and white uniform"></div>

    <div class="nurse-figure key" role="img" aria-label="Small nurse illustration for the Nursing Process key"></div>
    <svg class="key-icon" style="left:430px;top:765px" width="125" height="80" viewBox="0 0 125 80" aria-label="Nurse cap icon">
      <ellipse cx="62" cy="74" rx="45" ry="5" fill="url(#shadow)"/>
      <path d="M22,22 Q24,10 40,9 Q62,6 85,9 Q100,11 102,22 Q62,16 22,22 Z" fill="#dcdcdc"/>
      <path d="M25,34 Q62,24 99,34 L88,62 L36,62 Z" fill="#e6e6e6"/>
      <path d="M7,25 Q62,12 118,25 L114,33 Q62,22 11,33 Z" fill="#1f7fc8"/>
    </svg>
    <svg class="key-icon" style="left:750px;top:776px" width="92" height="74" viewBox="0 0 92 74" aria-label="Pyramid icon">
      <ellipse cx="46" cy="66" rx="40" ry="5" fill="url(#shadow)"/>
      <path d="M46,4 L83,60 L9,60 Z" fill="#239ddf"/>
    </svg>

    <section class="legend">
      <div class="legend-column process">
        <h2>Nursing Process</h2>
        <ul>
          <li>Assessment</li>
          <li>Nursing Diagnosis</li>
          <li>Planning</li>
          <li>Intervention</li>
          <li>Evaluation</li>
        </ul>
      </div>
      <div class="legend-column concepts">
        <h2>Core Concepts</h2>
        <ul>
          <li>Clinical Competence</li>
          <li>Critical Thinking</li>
          <li>Moral/Ethical Principles</li>
          <li>Growth Mindset</li>
          <li>Caring/Compassion</li>
          <li>Cultural Competence</li>
          <li>Effective Communication</li>
          <li>Life-long Learning</li>
        </ul>
      </div>
      <div class="legend-column needs">
        <h2>Brennick's Hierarchy<br>of Needs</h2>
        <ul>
          <li>Self-Actualization</li>
          <li>Esteem</li>
          <li>Love and Belonging</li>
          <li>Safety Needs</li>
          <li>Physiological Needs</li>
        </ul>
      </div>
    </section>
    <div class="footer-band"></div>
  </div>
</div>
</body>
</html>
```